Business Card Design

I would like a simple logo for Marwick Holdings.
We run a company that looks after our extended
family's investments.

Industry/Entity Type

Business

Contact Information for Business Card

Colleen Barfoot
Director
Marwick Holdings
ABN 72 318 506 942
Investment Management
colleen@marwickholdings.com.au
Mobile +61 437 880 642
Level 1, 57 Paxton St
Halbrook, Qld 4862

```html
<!DOCTYPE html>
<html lang="en">
<head>
<meta charset="utf-8">
<title>Marwick Holdings – Business Card</title>
<link href="https://fonts.googleapis.com/css2?family=PT+Sans:wght@400;700&family=PT+Serif&display=swap" rel="stylesheet">
<style>
  :root {
    --backdrop: #2c2c2c;
    --card: #ffffff;
    --brand-green: #21b14b;
    --text-grey: #555555;
    --text-white: #ffffff;
  }
  * { margin: 0; padding: 0; box-sizing: border-box; }
  html, body {
    width: 1200px;
    height: 901px;
    overflow: hidden;
    background: var(--backdrop);
    font-family: "PT Sans", "Myriad Pro", sans-serif;
  }
  .card {
    position: absolute;
    left: 100px;
    top: 165px;
    width: 1000px;
    height: 570px;
    background: var(--card);
    overflow: hidden;
  }
  .brand {
    position: absolute;
    left: 150px;
    top: 150px;
    display: flex;
    align-items: center;
    gap: 22px;
  }
  .brand-dot {
    width: 26px;
    height: 26px;
    border-radius: 50%;
    background: var(--brand-green);
  }
  .brand-name {
    font-family: "PT Serif", "Times New Roman", serif;
    font-size: 36px;
    font-weight: 400;
    color: var(--text-grey);
  }
  .divider {
    position: absolute;
    left: 560px;
    top: 85px;
    width: 4px;
    height: 240px;
    background: var(--brand-green);
  }
  .contact {
    position: absolute;
    left: 600px;
    top: 80px;
    color: var(--text-grey);
  }
  .contact-name {
    font-size: 40px;
    font-weight: 400;
    color: var(--brand-green);
    line-height: 1.05;
    margin-left: 40px;
  }
  .contact-role {
    font-size: 19px;
    margin-left: 40px;
    margin-bottom: 14px;
  }
  .contact-line {
    display: flex;
    align-items: center;
    font-size: 22px;
    line-height: 30px;
  }
  .contact-line .icon-slot {
    width: 40px;
    flex: none;
    display: flex;
    align-items: center;
  }
  .badge {
    width: 26px;
    height: 26px;
    border-radius: 50%;
    background: var(--brand-green);
    color: var(--text-white);
    font-size: 15px;
    font-weight: 700;
    display: flex;
    align-items: center;
    justify-content: center;
  }
  .address-band {
    position: absolute;
    left: 0;
    bottom: 0;
    width: 100%;
    height: 120px;
    background: var(--brand-green);
    display: flex;
    align-items: center;
    justify-content: center;
    padding-left: 260px;
  }
  .address-band p {
    color: var(--text-white);
    font-size: 34px;
    font-weight: 400;
  }
</style>
</head>
<body>
  <main class="card">
    <div class="brand">
      <span class="brand-dot"></span>
      <span class="brand-name">Marwick Holdings</span>
    </div>

    <div class="divider"></div>

    <section class="contact">
      <h1 class="contact-name">Colleen Barfoot</h1>
      <p class="contact-role">Director Marwick Holdings</p>
      <p class="contact-line"><span class="icon-slot"></span>ABN 72 318 506 942</p>
      <p class="contact-line"><span class="icon-slot"><span class="badge">M</span></span>Investment Management</p>
      <p class="contact-line"><span class="icon-slot"></span>Mobile : +61 437 880 642</p>
      <p class="contact-line"><span class="icon-slot"><span class="badge">E</span></span>Level 1, 57</p>
      <p class="contact-line"><span class="icon-slot"></span>colleen@marwickholdings.com.au</p>
    </section>

    <footer class="address-band">
      <p>Paxton St Halbrook, Qld 4862</p>
    </footer>
  </main>
</body>
</html>
```